Deactivated Coal-Fired Power Plant to be redeveloped into a Green Energy Campus.

Want a striking business card statement that introduces our concept project to provide economic and community recovery to a former rural coal community in western PA.
Essentially 12 project representatives that will lead both the demolition of an existing power plant and the redevelopment to a new Green energy site.
Business Card should reflect our effort.
We are open to ideas.

Target Market(s)

Energy and Power Generation industries

Industry/Entity Type

Power Generation and Data Centers

Contact Information for Business Card

Included in uploaded materials

Font styles to use
Sans Serif
Other font styles liked:
• Arial, Calibri

Requirements
Must have
• Multiple colors

```html
<!DOCTYPE html>
<html lang="en">
<head>
<meta charset="utf-8">
<title>Ridgeline Renewal – Business Card</title>
<link href="https://fonts.googleapis.com/css2?family=Montserrat:wght@700&family=Open+Sans:wght@400&display=swap" rel="stylesheet">
<style>
  :root {
    --backdrop: #1c1c1c;
    --green-deep: #0f9646;
    --green-mid: #14b85a;
    --green-glow: #1cf57a;
    --ink: #0a0a0a;
    --paper: #ffffff;
  }
  * { margin: 0; padding: 0; box-sizing: border-box; }
  html, body {
    width: 1200px; height: 1200px; overflow: hidden;
    background: var(--backdrop);
  }
  .card {
    position: absolute; top: 303px; height: 593px;
    box-shadow: 4px 4px 6px rgba(0,0,0,0.7);
    overflow: hidden;
  }
  .card-front {
    left: 200px; width: 369px;
    background: radial-gradient(ellipse 70% 55% at 50% 50%, var(--green-glow) 0%, var(--green-mid) 55%, var(--green-deep) 100%);
  }
  .plant-silhouette-art {
    position: absolute; left: 40px; top: 0; width: 310px; height: 593px;
    background: linear-gradient(180deg, rgba(12,130,60,0.10) 0%, rgba(12,130,60,0.22) 55%, rgba(12,125,58,0.45) 100%);
  }
  .wordmark {
    position: absolute; left: 0; right: 0;
    font-family: "Montserrat", sans-serif; font-weight: 700;
    color: var(--ink); text-align: center; line-height: 1.05; letter-spacing: 0.5px;
  }
  .card-front .wordmark { top: 386px; font-size: 36px; }
  .card-back { left: 599px; width: 364px; background: var(--paper); }
  .card-back-top { position: absolute; left: 0; top: 0; width: 100%; height: 377px; }
  .card-back-top .wordmark { top: 140px; font-size: 31px; }
  .rule-band { position: absolute; left: 0; top: 377px; width: 100%; height: 4px; background: var(--ink); }
  .contact-panel {
    position: absolute; left: 0; top: 381px; width: 100%; bottom: 0;
    background: radial-gradient(ellipse 70% 90% at 50% 90%, var(--green-glow) 0%, var(--green-mid) 55%, var(--green-deep) 100%);
    color: var(--paper); text-align: center;
    font-family: "Open Sans", sans-serif;
  }
  .contact-name {
    position: absolute; left: 0; right: 0; top: 44px;
    font-family: "Montserrat", sans-serif; font-weight: 700; font-size: 20px; letter-spacing: -0.3px;
  }
  .contact-title { position: absolute; left: 0; right: 0; top: 69px; font-size: 15px; }
  .contact-divider {
    position: absolute; left: 139px; top: 101px; width: 87px; height: 1.5px; background: var(--paper);
  }
  .contact-phone { position: absolute; left: 0; right: 0; top: 112px; font-size: 15px; }
  .contact-email { position: absolute; left: 0; right: 0; top: 134px; font-size: 15px; }
</style>
</head>
<body>
  <section class="card card-front">
    <div class="plant-silhouette-art" role="img" aria-label="Faint silhouettes of power plant smokestacks and cooling towers"></div>
    <div class="wordmark">RIDGELINE<br>RENEWAL</div>
  </section>

  <section class="card card-back">
    <div class="card-back-top">
      <div class="wordmark">RIDGELINE<br>RENEWAL</div>
    </div>
    <div class="rule-band"></div>
    <div class="contact-panel">
      <p class="contact-name">DANIEL CORWIN</p>
      <p class="contact-title">Chief Redevelopment LLC</p>
      <div class="contact-divider"></div>
      <p class="contact-phone">555.014.2200</p>
      <p class="contact-email">dcorwin@ridgelinerenewal.com</p>
    </div>
  </section>
</body>
</html>
```